Meadowlark Learning Growth Partners (MLGP)

This is a professional business card. Logo and picture are a must on the front of the card. I am an educational consultant. I have been consulting for the past three years for a company. I am now opening my own company. My goal for my consulting company is to eventually consult all over America.

Target Market(s)

Educators, schools, professionals

Industry/Entity Type

Consulting

Contact Information for Business Card

Picture/logo on front, simple modern design

Font styles to use
Serif

Colors
85abd2
0355a3
3176b5
cedeed

Requirements
Must have
• picture, logo,
• Odessa Pruitt, Ed.S
• address 5073 Cormorant ridge Dr. Nashville, TN 37940
• Cell:616-555-0148
• Office: 629-555-0172
• www.Mlgpedu.example
• pruittodessa@mailbox.example

```html
<!DOCTYPE html>
<html lang="en">
<head>
<meta charset="utf-8">
<title>Meadowlark Learning Growth Partners – Business Card</title>
<link href="https://fonts.googleapis.com/css2?family=Merriweather:ital,wght@0,400;0,700;0,900;1,700&display=swap" rel="stylesheet">
<style>
  :root {
    --navy: #213f7d;
    --band: #1f3d7c;
    --photo-blue: #3176b5;
    --photo-deep: #0355a3;
    --sky: #cedeed;
    --mist: #85abd2;
    --white: #ffffff;
    --stage: #e9edf2;
  }
  * { margin: 0; padding: 0; box-sizing: border-box; }
  html, body { width: 1200px; height: 1000px; overflow: hidden; }
  body {
    background: var(--stage);
    font-family: "Merriweather", Georgia, serif;
    position: relative;
  }
  .card {
    position: absolute;
    left: 250px;
    width: 700px;
    height: 400px;
    border-radius: 18px;
    overflow: hidden;
    box-shadow: 0 10px 30px rgba(20, 40, 80, 0.18);
  }

  /* Contact side */
  .card--contact { top: 70px; background: var(--white); }
  .contact__header {
    position: absolute; left: 0; top: 0; width: 100%; height: 108px;
    background: var(--white);
  }
  .contact__name {
    position: absolute; left: 42px; top: 40px;
    font-style: italic; font-weight: 700; font-size: 21px;
    color: var(--navy);
  }
  .brand {
    position: absolute; right: 36px; top: 20px;
    display: flex; align-items: center; color: var(--navy);
  }
  .brand__mark {
    font-weight: 900; font-size: 30px; letter-spacing: 3px;
    padding-right: 14px;
  }
  .brand__divider { width: 2px; height: 72px; background: var(--navy); }
  .brand__full {
    padding-left: 12px;
    font-weight: 700; font-size: 13px; line-height: 16px;
  }
  .contact__band {
    position: absolute; left: 0; top: 108px; width: 100%; height: 266px;
    background: var(--band);
  }
  .contact__list {
    position: absolute; left: 44px; top: 30px;
    list-style: none; color: var(--white); font-size: 15px;
  }
  .contact__list li {
    display: flex; align-items: center; height: 25px;
  }
  .contact__list svg { width: 16px; height: 16px; margin-right: 12px; flex: none; }
  .contact__address {
    position: absolute; right: 34px; bottom: 26px;
    text-align: right; color: var(--white); font-size: 16px; line-height: 24px;
  }

  /* Photo side */
  .card--front { top: 530px; background: var(--sky); }
  .front__brand {
    position: absolute; left: 60px; top: 140px;
    font-weight: 900; font-size: 92px; letter-spacing: 6px;
    color: var(--navy);
  }
  .front__art { position: absolute; inset: 0; }
</style>
</head>
<body>

  <section class="card card--contact" aria-label="Business card, contact side">
    <header class="contact__header">
      <h1 class="contact__name">Odessa Pruitt, Ed.S</h1>
      <div class="brand">
        <span class="brand__mark">MLGP</span>
        <span class="brand__divider"></span>
        <span class="brand__full">Meadowlark<br>Learning<br>Growth<br>Partners</span>
      </div>
    </header>

    <div class="contact__band">
      <ul class="contact__list">
        <li>
          <svg viewBox="0 0 16 16" fill="none" stroke="#fff" stroke-width="1.4"><rect x="4" y="1" width="8" height="14" rx="1.5"/><line x1="7" y1="12.5" x2="9" y2="12.5"/></svg>
          616-555-0148
        </li>
        <li>
          <svg viewBox="0 0 16 16" fill="#fff"><path d="M4 1.5l2.2 3-1.3 1.6c.8 2 2.4 3.6 4.4 4.4l1.6-1.3 3 2.2-1.2 2.6C7 13.6 2.4 9 1.4 3.7z"/></svg>
          629-555-0172
        </li>
        <li>
          <svg viewBox="0 0 16 16" fill="none" stroke="#fff" stroke-width="1.2"><circle cx="8" cy="8" r="6.5"/><ellipse cx="8" cy="8" rx="3" ry="6.5"/><line x1="1.5" y1="8" x2="14.5" y2="8"/></svg>
          www.Mlgpedu.example
        </li>
        <li>
          <svg viewBox="0 0 16 16" fill="#fff"><path d="M1 3.5h14v9H1z"/><path d="M1 3.5l7 5 7-5" fill="none" stroke="#1f3d7c" stroke-width="1.2"/></svg>
          pruittodessa@mailbox.example
        </li>
      </ul>
      <p class="contact__address">5073 Cormorant ridge<br>Dr. Nashville, TN 37940</p>
    </div>
  </section>

  <section class="card card--front" aria-label="Business card, photo side">
    <svg class="front__art" viewBox="0 0 700 400" width="700" height="400">
      <defs>
        <radialGradient id="portraitTone" cx="0.55" cy="0.45" r="0.7">
          <stop offset="0" stop-color="#3a7fc0"/>
          <stop offset="1" stop-color="#0355a3"/>
        </radialGradient>
      </defs>
      <circle cx="790" cy="300" r="410" fill="#ffffff"/>
      <g role="img" aria-label="Portrait photograph of the consultant against a blue backdrop">
        <circle cx="810" cy="310" r="390" fill="url(#portraitTone)"/>
      </g>
    </svg>
    <span class="front__brand">MLGP</span>
  </section>

</body>
</html>
```